Bulldog themed background for Real Estate Purchase Letter

I need a phantom background or watermark on a standard 8 1/2" x 11" paper. I am going to put a letter over the background. I want a bulldog theme that is cute, funny and original. This letter is for a real estate project and we want to capture the person sub-consciously . Attached is my personal dogs. If you want to use them you can but not required. I have attached the letter that I am trying to emulate. I want bulldogs not horses.

Target Market(s)

45 years old and higher

Industry/Entity Type

Real Estate

Font styles to use
Serif
Sans Serif

Colors

Designer to choose colors to be used in the design.

Requirements
Must have
• fun, happiness, reassuring,
Should not have
• violence, negativity, unhappy

```html
<!DOCTYPE html>
<html lang="en">
<head>
<meta charset="utf-8">
<title>Bulldog Purchase Letter</title>
<link href="https://fonts.googleapis.com/css2?family=Source+Sans+3:wght@400&display=swap" rel="stylesheet">
<style>
  :root {
    --paper: #ffffff;
    --sun-yellow: #f4d13d;
    --paw-gold: #dcb020;
    --ink-dark: #333333;
    --note-red: #d7143a;
    --sign-blue: #2b7fc3;
    --rule-black: #0d0d0d;
    --photo-fur: #e9e4dc;
    --photo-shade: #7a6e62;
  }
  * { box-sizing: border-box; margin: 0; padding: 0; }
  html, body { width: 947px; height: 1200px; overflow: hidden; background: var(--paper); }
  body { font-family: "Source Sans 3", "Myriad Pro", Arial, sans-serif; color: var(--ink-dark); }

  .letter-page { position: relative; width: 947px; height: 1200px; overflow: hidden; background: var(--paper); }

  .top-band { position: absolute; left: 0; top: 0; width: 100%; height: 19px; background: var(--sun-yellow); }

  .note { color: var(--note-red); font-size: 18.5px; line-height: 25.5px; position: absolute; }
  .recipient-address { left: 41px; top: 96px; }
  .agent-note { left: 717px; top: 96px; }
  .salutation { left: 42px; top: 225px; }

  .letter-body { position: absolute; left: 72px; top: 258px; width: 834px; font-size: 18px; line-height: 25.5px; }
  .letter-body p { text-align: justify; margin-bottom: 25.5px; }

  .closing { position: absolute; left: 71px; top: 738px; font-size: 18px; }
  .sign-hint { position: absolute; left: 287px; top: 777px; font-size: 18px; color: var(--sign-blue); }
  .signer { position: absolute; left: 72px; top: 815px; font-size: 18px; line-height: 25.5px; }

  .postscript { left: 72px; top: 1003px; width: 450px; }
  .mailing-note { left: 72px; top: 1105px; }

  .bulldog-frame { position: absolute; left: 548px; top: 624px; width: 496px; height: 496px; }

  .bottom-rule { position: absolute; left: 0; top: 1137px; width: 100%; height: 6px; background: var(--rule-black); }
  .paw-band { position: absolute; left: 0; top: 1143px; width: 100%; height: 57px; background: linear-gradient(180deg, var(--sun-yellow), #efc932); }
</style>
</head>
<body>
<main class="letter-page">
  <div class="top-band"></div>

  <div class="note recipient-address">Mr Outta State Owner - PA Address<br>4821 Cedar Lane<br>LAKEVIEW FL 32000-0000</div>
  <div class="note agent-note">Must include licensed<br>real estate agent</div>

  <div class="note salutation">Dear Homeowner,</div>

  <section class="letter-body">
    <p>I am writting you, because I am interested in purchasing your property located at PA Address. I live nearby in Millbrook and I purchase properties throughout the state of PA. Curently, I am working on projects in the neighborhod, Which is how I learned of your property.</p>
    <p>Please call me at (xxx) xxxx-xxxx, so I can tell you how we ca buy your property quickly, with no hassles and most importantly, at a fair price. I purchase the house directly from you, so there are no real estate commissions or extra fees coming out of your pocket. Furthermore, I always make cash offers. so you never have to worry about delays resulting from a buyer trying to qualify for a mortgage and wasting your valuable time.</p>
    <p>I’ll be glade to personally tell you more about how we can work together. All calls are completely confidential and there is no obligation whatsoever. Even if you are not interested in selling at this time, call (xxx) xxxx-xxxx, so I can help you with determining the value of your property. You should also keep this letter for future reference, since things in life have a tendency to change unexpectedly. Thank you for your time and consideration and I look forward to speaking with you.</p>
  </section>

  <div class="closing">Sincerely,</div>
  <div class="sign-hint">(Sign in Blue Ink)</div>
  <div class="signer">Dana Whitfield<br>(xxx) xxxx-xxxx</div>

  <svg class="bulldog-frame" viewBox="0 0 496 496" aria-hidden="false">
    <defs>
      <radialGradient id="furTone" cx="50%" cy="45%" r="60%">
        <stop offset="0%" stop-color="var(--photo-fur)"/>
        <stop offset="70%" stop-color="#d8d0c4"/>
        <stop offset="100%" stop-color="var(--photo-shade)"/>
      </radialGradient>
    </defs>
    <circle cx="248" cy="248" r="245" fill="none" stroke="var(--sun-yellow)" stroke-width="5"/>
    <circle cx="248" cy="248" r="236" fill="url(#furTone)" role="img" aria-label="Photo of a sleepy white bulldog with its tongue out"/>
  </svg>

  <div class="note postscript">P.S. If you would like to e-mail me information and pictures of your property, please send them to dana.offers@mailbox.example</div>
  <div class="note mailing-note">Do not use lable for return address, name write.</div>

  <div class="bottom-rule"></div>
  <div class="paw-band" role="img" aria-label="Repeating pattern of golden paw prints"></div>
</main>
</body>
</html>
```